EOFYS BANNER REQUIRED FOR HIGH-END BABY PRODUCT

We seel baby beanbags, and we need a banner for our annual END OF FINANCIAL YEAR SALE (EOFYS) about 700x900px.

The promo will be:

THE EOFYS SALE IS ON NOW!
30% OFF ALL ORDERS OVER $149 WITH CODE: EOFYS

We will use this banner for an email marketing campaign, and we will actually need to resize this banner to suit some affiliate marketing sizes too (ie: leaderboard etc), so if you are able to show your design in a few different sizes, that would be great.

We don't have alot of images for you to work off, so it will be your creative design skills that make it great.

Please keep in mind this is for a massive event that we will be competing with alot of other businesses for, as it is an annual event where the whole country goes on sale. We are in the process of building a photo studio so we have attached the images we have to work with now.

I have uploaded some of our patterns for you. This is CONFIDENTIAL. You are welcome to use these patterns in the dsign if you like.

Please, do your best.

Urban mums who crave design and function more than a cheap product.

Baby

• montserrat; intro rust; Pirou

b768aa
e667a6
f68e4e
fece3e
fbf289
add136
cadf82
33b8a4
33a6d7

• One, or both, of the two images upload. They are: IMG.5251 / IMG. 5253
• Would love a toddler in the pic also, if possible...they don't have to be using our beanbag, but there should be a pic of our beanbag there, as if it is waiting for them to use.
• Other brands. Childish themes. Too much vector overload...but some is awesome.

```html
<!DOCTYPE html>
<html lang="en">
<head>
<meta charset="utf-8">
<title>EOFYS Sale Banner</title>
<link rel="stylesheet" href="https://fonts.googleapis.com/css2?family=Fredoka:wght@600;700&family=Montserrat:wght@500;600&display=swap">
<style>
  :root {
    --lime: #add136;
    --lime-soft: #b7d86a;
    --sky: #33a6d7;
    --sky-light: #5cbde6;
    --pink: #e667a6;
    --purple: #8e3fa6;
    --purple-light: #b768aa;
    --yellow: #fbf289;
    --yellow-deep: #fece3e;
    --white: #ffffff;
    --cream: #f4eedd;
  }
  * { margin: 0; padding: 0; box-sizing: border-box; }
  html, body { width: 933px; height: 1200px; overflow: hidden; }
  body { background: var(--lime-soft); }
  .banner {
    position: relative;
    width: 933px;
    height: 1200px;
    overflow: hidden;
    background: var(--lime-soft);
    font-family: "Fredoka", "Arial Rounded MT Bold", sans-serif;
  }
  .banner__bands { position: absolute; inset: 0; }
  .headline { position: absolute; left: 50px; top: 140px; width: 460px; text-align: center; }
  .headline__lead {
    color: var(--pink);
    font-size: 70px;
    font-weight: 700;
    letter-spacing: 4px;
    line-height: 1;
  }
  .headline__main {
    color: var(--purple);
    font-size: 184px;
    font-weight: 700;
    line-height: 0.95;
    letter-spacing: 4px;
    margin-top: 8px;
    -webkit-text-stroke: 3px var(--white);
    paint-order: stroke fill;
  }
  .headline__tail {
    color: var(--pink);
    font-size: 52px;
    font-weight: 700;
    letter-spacing: 11px;
    line-height: 1;
    margin-top: 12px;
  }
  .badge { position: absolute; left: 548px; top: 222px; width: 358px; height: 358px; }
  .badge__text {
    position: absolute; inset: 0;
    display: flex; flex-direction: column; align-items: center; justify-content: center;
    transform: rotate(-6deg);
  }
  .badge__value { color: var(--white); font-size: 86px; font-weight: 700; line-height: 1; }
  .badge__label { color: var(--yellow); font-size: 76px; font-weight: 600; line-height: 1; }
  .product-photo {
    position: absolute;
    border-radius: 40px;
  }
  .product-photo--seat {
    left: 53px; top: 520px; width: 360px; height: 347px;
    background: radial-gradient(ellipse at 50% 40%, #f7f3f8 0%, #efe3c8 60%, #e2c98e 100%);
  }
  .product-photo--nest {
    left: 455px; top: 640px; width: 432px; height: 360px;
    background: radial-gradient(ellipse at 50% 35%, #fbf8ef 0%, #f1e7cf 60%, #e0c78f 100%);
  }
  .offer {
    position: absolute; left: 47px; top: 950px;
    font-family: "Montserrat", Arial, sans-serif;
    font-weight: 500;
    font-size: 47px;
    line-height: 62px;
    letter-spacing: 1px;
    color: var(--white);
  }
  .offer__code { color: var(--yellow); font-weight: 600; }
</style>
</head>
<body>
  <main class="banner">
    <svg class="banner__bands" width="933" height="1200" viewBox="0 0 933 1200" aria-hidden="true">
      <polygon points="0,560 933,920 933,946 0,586" fill="var(--yellow)"/>
      <polygon points="0,586 933,946 933,966 0,606" fill="var(--purple-light)"/>
      <polygon points="0,606 933,966 933,986 0,626" fill="var(--lime)"/>
      <polygon points="0,626 933,986 933,1200 0,1200" fill="var(--sky)"/>
    </svg>

    <header class="headline">
      <p class="headline__lead">THE EOFYS</p>
      <h1 class="headline__main">SALE</h1>
      <p class="headline__tail">IS ON NOW!</p>
    </header>

    <div class="badge">
      <svg width="358" height="358" viewBox="-180 -180 360 360" aria-hidden="true">
        <defs>
          <radialGradient id="badgeFill" cx="40%" cy="35%" r="70%">
            <stop offset="0" stop-color="#b24fc4"/>
            <stop offset="1" stop-color="#6f2a8f"/>
          </radialGradient>
        </defs>
        <polygon fill="url(#badgeFill)" stroke="#ffffff" stroke-width="5"
          points="0,-172 20,-152 44,-166 58,-141 86,-149 92,-121 121,-121 119,-92 146,-82 135,-55 157,-38 138,-17 154,6 130,21 140,48 112,57 114,86 85,89 78,117 51,109 34,134 14,115 -10,134 -25,110 -51,121 -62,95 -91,99 -92,70 -121,63 -112,35 -137,21 -120,-3 -140,-23 -116,-40 -126,-67 -98,-75 -100,-105 -71,-109 -63,-137 -36,-126 -18,-151"/>
      </svg>
      <div class="badge__text">
        <span class="badge__value">30%</span>
        <span class="badge__label">Off</span>
      </div>
    </div>

    <div class="product-photo product-photo--seat" role="img" aria-label="Baby reclining in a bird-print beanbag on a rocking frame"></div>
    <div class="product-photo product-photo--nest" role="img" aria-label="Newborn lying in a bird-print beanbag bassinet on a rocking frame"></div>

    <p class="offer">ALL ORDERS<br>OVER $149 WITH<br><span class="offer__code">CODE: EOFYS</span></p>
  </main>
</body>
</html>
```